Dane Morrow films- wedding and event films company website. DESKTOP AND MOBILE

We need a website for a high-end wedding and event film production company. Looking for a very modern and elegant design. my old website is www.danemorrowfilms.example

I like the "white/black/rose gold" color scheme of my logo.

really looking for a sleek modern design the breaths professional and artistic.

Target Market(s)

wedding and event films.

Industry/Entity Type

Film Production

Number of Pages Required

5+ page

Colors

Designer to choose colors to be used in the design.

Requirements
Must have
• website name will be www.danemorrowfilms.example
• tagline is "CINEMATIC STORIES ABOUT YOU"
• sections: HOME, CONTACT, ABOUT, FILMS, BLOG
• You can see my old website at danemorrowfilms.example
• Website about section:
• Dane Morrow Films was Established with the basis of truly cinematic and artistic films in mind. Dane and his team routinely travel the globe documenting weddings and events for high profile clients and discerning couples. Dane was born and raised in Maui Hawaii and has a unique approach to his films that embody the essence of a Hollywood film. Dane has spent the last 10 years traveling the world documenting corporate events and weddings with multiple Award winning production companies. In 2017 Dane decided to establish his own brand “Dane Morrow films” that will take everything he has learned with his past experiences and push it to the next level. Aside from his personal achievements, Dane is extremely passionate about his craft and always looks forward to handcrafting beautiful wedding/event films for his clients. The style of work is non-traditional and the day of filming is extremely unobtrusive (as we are looking for natural-candid/ raw emotions).
• If you are looking for the best price in town, we are probably not the best option, but if you’re looking for the best quality and peace of mind on your wedding day, then you’re in the right place. Dane Morrow Films is a boutique studio that only accepts a limited number of assignments per year. Inquire early to ensure availability.
• LINKS TO REELHOUSE VIDEOS THAT WILL BE IN THE "FILMS' SECTION.
• BRENT FILM TRAILER - https://clipvault.example/508114362
• BRENT FEATURE FILM - https://clipvault.example/617392048
• JUNE AND ROB'S WEDDING - https://clipvault.example/724958160
• DRONE DEMO REEL - https://clipvault.example/841576203
• WEDDING INDUSTRY EVENT PARTY - https://clipvault.example/962304817/a8d3e7b21c
• images that you can use on site are here: https://brigittolsenimages.proofbox.example/gallery/nora&felix/
• password is: meadow

```html
<!DOCTYPE html>
<html lang="en">
<head>
<meta charset="utf-8">
<title>About — Dane Morrow Films</title>
<link href="https://fonts.googleapis.com/css2?family=Open+Sans:wght@400;600;700&family=Pathway+Gothic+One&family=Share+Tech+Mono&display=swap" rel="stylesheet">
<style>
:root{
  --accent:#e6a06a;
  --white:#ffffff;
  --text:#e8e8e8;
  --muted:#5d5d5d;
  --hero-top:#1b2b35;
  --hero-bottom:#0a0a0a;
  --about-bg:#2b2b2b;
  --features-bg:#292929;
  --note-bg:#252525;
  --footer-bg:#212121;
}
*{margin:0;padding:0;box-sizing:border-box}
html,body{width:829px;height:1200px;overflow:hidden;background:var(--footer-bg)}
body{font-family:"Open Sans",sans-serif;color:var(--text);position:relative}
.hero{position:absolute;left:0;top:0;width:829px;height:430px;
  background:radial-gradient(ellipse at 50% 20%,#24384a 0%,transparent 65%),linear-gradient(180deg,var(--hero-top) 0%,#16222a 45%,var(--hero-bottom) 85%)}
.hero-photo{position:absolute;inset:0}
.brand{position:absolute;left:60px;top:22px;display:flex;align-items:center;gap:5px;
  font-family:"Open Sans",sans-serif;font-size:7px;font-weight:600;letter-spacing:.8px;color:var(--white)}
.brand-mark{width:12px;height:12px;border:1px solid var(--white);border-radius:50%}
.nav{position:absolute;top:25px;left:0;width:829px;font-family:"Share Tech Mono",monospace;font-size:10px;letter-spacing:1px;color:var(--white)}
.nav a{position:absolute;color:inherit;text-decoration:none}
.nav a.active{color:var(--accent)}
.hero-title{position:absolute;top:193px;left:0;width:829px;text-align:center;font-family:"Pathway Gothic One",sans-serif;font-size:38px;letter-spacing:3px;color:var(--white);font-weight:400}
.about{position:absolute;left:0;top:430px;width:829px;height:296px;background:var(--about-bg)}
.about-copy{position:absolute;left:60px;top:34px;width:458px;font-size:9.6px;line-height:13.8px}
.about-copy h2{font-size:11.5px;font-weight:700;color:var(--white);margin-bottom:10px}
.about-copy p{margin-bottom:13.6px}
.portrait{position:absolute;left:544px;top:36px;width:224px;height:224px;background:radial-gradient(circle at 55% 45%,#8a8a8a 0%,#5a5a5a 45%,#2e2e2e 100%)}
.features{position:absolute;left:0;top:726px;width:829px;height:295px;background:var(--features-bg)}
.feature{position:absolute;top:100px;width:180px;text-align:center;font-size:9.6px;line-height:11.5px;color:var(--white)}
.feature svg{display:block;margin:0 auto 18px;width:24px;height:24px}
.feature h3{font-size:9.8px;font-weight:700}
.note{position:absolute;left:0;top:1021px;width:829px;height:107px;background:var(--note-bg);display:flex;align-items:center;justify-content:center}
.note p{width:540px;text-align:center;font-size:9.6px;line-height:13.8px}
.footer{position:absolute;left:0;top:1128px;width:829px;height:72px;background:var(--footer-bg)}
.copyright{position:absolute;left:60px;top:29px;font-size:9.6px;color:var(--muted)}
.footer-brand{position:absolute;left:0;width:829px;top:30px;display:flex;justify-content:center;align-items:center;gap:5px;font-size:7px;font-weight:600;letter-spacing:.8px;color:var(--white)}
.footer-brand .brand-mark{border-color:var(--accent)}
.social{position:absolute;right:60px;top:30px;display:flex;gap:18px;font-size:8px;color:var(--muted)}
</style>
</head>
<body>
<header class="hero">
  <div class="hero-photo" role="img" aria-label="Silhouettes of a group of friends against a dusky evening sky"></div>
  <div class="brand"><span class="brand-mark"></span>DANE MORROW</div>
  <nav class="nav">
    <a style="left:498px">HOME</a>
    <a class="active" style="left:554px">ABOUT</a>
    <a style="left:614px">FILMS</a>
    <a style="left:675px">CONTACT</a>
    <a style="left:747px">BLOG</a>
  </nav>
  <h1 class="hero-title">ABOUT</h1>
</header>

<section class="about">
  <div class="about-copy">
    <h2>Dane Morrow Films</h2>
    <p>was Established with the basis of truly cinematic and artistic films in mind. Dane and his team routinely travel the globe documenting weddings and events for high profile clients and discerning couples. Dane was born and raised in Maui Hawaii and has a unique approach to his films that embody the essence of a Hollywood film. Dane has spent the last 10 years traveling the world documenting corporate events and weddings with multiple Award winning production companies.</p>
    <p>&nbsp;In 2017 Dane decided to establish his own brand “Dane Morrow films” that will take everything he has learned with his past experiences and push it to the next level. Aside from his personal achievements, Dane is extremely passionate about his craft and always looks forward to handcrafting beautiful wedding/event films for his clients. The style of work is non-traditional and the day of filming is extremely unobtrusive (as we are looking for natural-candid/ raw emotions).</p>
  </div>
  <div class="portrait" role="img" aria-label="Black and white portrait of the filmmaker"></div>
</section>

<section class="features">
  <div class="feature" style="left:82px">
    <svg viewBox="0 0 24 24" fill="none" stroke="#e6a06a" stroke-width="1.2" stroke-linejoin="round"><rect x="2" y="10" width="4" height="11"/><path d="M6 11l4-5 1-4c2 0 3 2 2 6h7c1 0 2 1 1.6 2.2l-2 8.3c-.3 1-1 1.5-2 1.5H6"/></svg>
    <h3>Best Quality</h3>
    We always guarantee the best<br>quality for our customers
  </div>
  <div class="feature" style="left:324px">
    <svg viewBox="0 0 24 24" fill="none" stroke="#e6a06a" stroke-width="1.2" stroke-linejoin="round"><rect x="2" y="6" width="20" height="14" rx="1.5"/><path d="M8 6l1.5-2.5h5L16 6"/><circle cx="12" cy="13" r="4"/><rect x="4" y="8" width="3" height="1.6"/></svg>
    <h3>Best Profession</h3>
    We always guarantee the best<br>quality for our customers
  </div>
  <div class="feature" style="left:566px">
    <svg viewBox="0 0 24 24" fill="none" stroke="#e6a06a" stroke-width="1.2" stroke-linejoin="round"><path d="M2 10l5-6 4 2 3-1 4 2 4 4"/><path d="M5 12l6 7c1 1 2 1 3 0l6-6"/><path d="M11 6l-3 4c1 1 2 1 3 0l2-2"/><path d="M9 15l2 2M11 13l2 2M13 11l2 2"/></svg>
    <h3>Best Satisfied</h3>
    100% customer satisfaction
  </div>
</section>

<section class="note">
  <p>If you are looking for the best price in town, we are probably not the best option, but if you’re looking for the best quality and peace of mind on your wedding day, then you’re in the right place. Dane Morrow Films is a boutique studio that only accepts a limited number of assignments per year. Inquire early to ensure availability.</p>
</section>

<footer class="footer">
  <div class="copyright">Copyright by DANE MORROW &nbsp;© 2015</div>
  <div class="footer-brand"><span class="brand-mark"></span>DANE MORROW</div>
  <div class="social"><span>Frameline</span><span>Chirpwell</span><span>Reelhouse</span></div>
</footer>
</body>
</html>
```